Website design needed for Renewable utilities company based in New Zealand.

Website design needed for Lanternvale Holdings based in New Zealand.

Please see attached logo.

We sell solar panels, vertical axis wind turbines, atmospheric water generators and other related equipment for those who don't have access or don't want to depend on the government, city councils for their utilities (power and water).

We like metallic texture, dark grey and purple, red or blue colours. The design should go well with the attached logo.

Target Market(s)

The Eco conscious

Industry/Entity Type

Government

Logo Text

Lanternvale Summit

Requirements
Must have
• Must Have:
- Metallic finish is a must.
- Design should fit around the attached logo well.
Nice to have
• Sharpe design prefred rather than rounded edges

```html
<!DOCTYPE html>
<html lang="en">
<head>
<meta charset="utf-8">
<title>Lanternvale Summit – Home Solar Panels</title>
<link rel="stylesheet" href="https://fonts.googleapis.com/css2?family=Arimo:wght@400;700&family=Crimson+Pro:wght@400;500&display=swap">
<style>
  :root {
    --white: #ffffff;
    --ink: #333333;
    --body-grey: #8a8a8a;
    --nav-active: #6b6f8a;
    --nav-idle: #c6c6c6;
    --brand-blue: #1f5fa8;
    --button-top: #2a8fd6;
    --button-bottom: #0a5aa8;
    --page-top: #b8af9f;
    --page-bottom: #faf9f6;
    --news-top: #a9a9a9;
    --news-bottom: #6c6c6c;
    --news-gold: #d9bb7e;
    --footer-grey: #c9c9c9;
    --footer-ink: #4a4a4a;
    --copyright: #8a5a2e;
    --search-bg: #faf3e8;
    --go-bg: #5d5d5d;
    --badge-ring: #e8e8e8;
    --sans: "Arimo", Arial, sans-serif;
    --serif: "Crimson Pro", Georgia, serif;
  }
  * { box-sizing: border-box; margin: 0; padding: 0; }
  html, body { width: 1024px; height: 1200px; overflow: hidden; }
  body {
    position: relative;
    font-family: var(--sans);
    color: var(--ink);
    background: linear-gradient(to bottom, var(--white) 0, var(--white) 178px, var(--page-top) 178px, var(--page-bottom) 1200px);
  }
  .abs { position: absolute; }

  /* Header */
  .brand { left: 62px; top: 50px; width: 160px; height: 90px; }
  .brand-mark { left: 42px; top: 0; width: 52px; height: 52px; border-radius: 50%; background: var(--brand-blue); }
  .brand-name { left: 0; top: 62px; width: 150px; text-align: center; font-size: 18px; color: var(--brand-blue); white-space: nowrap; }
  .brochure-btn {
    left: 772px; top: 18px; width: 193px; height: 39px; border-radius: 20px;
    background: linear-gradient(var(--button-top), var(--button-bottom));
    box-shadow: 0 2px 3px rgba(0,0,0,.35);
    color: var(--white); font-size: 16px; line-height: 39px; text-align: center; text-decoration: none;
  }
  .main-nav { left: 328px; top: 83px; display: flex; gap: 13px; font-size: 19px; font-weight: 700; }
  .main-nav a { color: var(--nav-idle); text-decoration: none; }
  .main-nav a.is-active { color: var(--nav-active); }

  /* Content sheet */
  .sheet { left: 36px; top: 178px; width: 952px; height: 848px; background: var(--white); }

  .hero-photo {
    left: 36px; top: 184px; width: 952px; height: 286px;
    background: linear-gradient(160deg, #9cc6ea 0%, #c7def3 30%, #4a4c52 55%, #2f3e6e 80%, #9bbde0 100%);
  }
  .hero-lines { right: 329px; top: 192px; text-align: right; color: var(--white); font-size: 28px; line-height: 35px; letter-spacing: .3px; text-shadow: 0 1px 3px rgba(0,0,0,.6), 0 0 6px rgba(0,0,0,.3); }
  .hero-callout {
    left: 724px; top: 268px; transform: rotate(-36deg); transform-origin: left top;
    color: var(--white); font-weight: 700; font-size: 24px; line-height: 24px; text-align: center;
    text-shadow: 0 0 3px #9b3fbf, 0 0 3px #9b3fbf;
  }
  .badge {
    width: 126px; height: 126px; border-radius: 50%; top: 380px;
    background: radial-gradient(circle, var(--white) 60%, var(--badge-ring) 100%);
    box-shadow: 0 2px 5px rgba(0,0,0,.25);
  }
  .badge-core {
    position: absolute; left: 10px; top: 10px; width: 106px; height: 106px; border-radius: 50%;
    color: var(--white); text-align: center; font-weight: 700; text-shadow: 0 1px 2px rgba(0,0,0,.35);
  }
  .badge-earn { left: 492px; }
  .badge-earn .badge-core { background: radial-gradient(circle at 50% 30%, #e6f27a, #9cc316); }
  .badge-save { left: 634px; }
  .badge-save .badge-core { background: radial-gradient(circle at 50% 30%, #4fd0f4, #0783c9); }
  .badge-avg { left: 776px; }
  .badge-avg .badge-core { background: radial-gradient(circle at 50% 30%, #8ab4ec, #2f62b8); }

  .thumb { top: 521px; width: 216px; height: 131px; }
  .thumb-a { left: 38px; background: linear-gradient(160deg, #5a86c7, #1e2e66 60%, #b0a695); }
  .thumb-b { left: 262px; top: 523px; background: linear-gradient(#4f8fd9 0%, #d5e6f5 40%, #2f4c8a 60%, #4f6b3a 100%); }
  .thumb-c { left: 488px; top: 523px; background: linear-gradient(#2d63c6 0%, #6e9be0 50%, #f1c218 78%, #d39a10 100%); }

  /* Intro copy */
  .intro-title { left: 60px; top: 668px; font-size: 29px; font-weight: 400; color: var(--white); text-shadow: 0 0 4px #555, 0 0 8px #888; }
  .intro-sub { left: 60px; top: 711px; font-size: 21px; font-weight: 400; color: var(--white); text-shadow: 0 0 3px #666, 0 0 6px #999; }
  .story { left: 60px; width: 492px; }
  .story h3 { font-weight: 400; font-size: 16px; color: #222; margin-bottom: 6px; }
  .story p { font-size: 11.6px; line-height: 16px; color: var(--body-grey); }
  .story-1 { top: 747px; }
  .story-2 { top: 823px; }
  .story-3 { top: 918px; }
  .story-photo { left: 572px; width: 125px; height: 62px; }
  .story-photo-1 { top: 748px; background: linear-gradient(#3b7fd0, #cfe0f0 55%, #5f7a3f); }
  .story-photo-2 { top: 847px; background: linear-gradient(135deg, #b8d8f4, #2d5fb0 60%, #1a3470); }
  .story-photo-3 { left: 571px; top: 942px; background: linear-gradient(#7fb5e6, #3d5f9a 55%, #2a3e6a); }

  /* News */
  .news { left: 713px; top: 524px; width: 270px; height: 306px; background: linear-gradient(var(--news-top), var(--news-bottom)); color: var(--white); }
  .news-photo { position: absolute; left: 20px; top: 0; width: 232px; height: 103px; background: linear-gradient(#5e97d8 0%, #f4f8fb 35%, #8a9aa8 60%, #4f9a2e 100%); }
  .news-label { position: absolute; left: 20px; top: 113px; font-size: 23px; color: var(--news-gold); }
  .news-head { position: absolute; left: 20px; top: 148px; width: 190px; font-size: 13.5px; font-weight: 700; line-height: 18px; }
  .news-date { position: absolute; left: 218px; top: 152px; width: 40px; text-align: center; font-size: 12px; font-weight: 700; line-height: 12px; }
  .news-text { position: absolute; left: 20px; top: 188px; width: 190px; font-size: 12px; line-height: 18px; }
  .news-more { position: absolute; left: 20px; top: 269px; font-family: var(--serif); font-size: 17px; color: var(--white); text-decoration: none; }

  .helpline { left: 714px; top: 847px; width: 269px; height: 120px; background: radial-gradient(circle at 30% 40%, #ffffff, #a9d2f2 45%, #3f8ed6 100%); }

  /* Footer */
  .footer { left: 36px; top: 1026px; width: 947px; height: 138px; background: var(--footer-grey); }
  .footer-links { position: absolute; right: 11px; top: 10px; display: flex; gap: 12px; font-family: var(--serif); font-size: 18px; }
  .footer-links a { color: var(--footer-ink); text-decoration: none; }
  .copyright { position: absolute; left: 25px; top: 101px; font-family: var(--serif); font-size: 15px; color: var(--copyright); }
  .copyright span { color: #666; }
  .search-field { position: absolute; left: 411px; top: 93px; width: 218px; height: 24px; background: var(--search-bg); font-family: var(--serif); font-size: 15px; color: #b0a898; padding-left: 12px; line-height: 24px; }
  .search-go { position: absolute; left: 633px; top: 93px; width: 28px; height: 24px; background: var(--go-bg); color: var(--white); font-family: var(--serif); font-size: 14px; line-height: 24px; text-align: center; }
  .stay-label { position: absolute; left: 674px; top: 91px; width: 110px; height: 28px; border: 1px solid #ddd; font-family: var(--serif); font-size: 15px; color: var(--white); text-shadow: 0 0 2px #888; line-height: 26px; text-align: center; }
  .social { position: absolute; left: 798px; top: 93px; display: flex; gap: 5px; }
  .social span { width: 24px; height: 24px; display: block; }
</style>
</head>
<body>
  <header>
    <div class="abs brand">
      <span class="abs brand-mark"></span>
      <span class="abs brand-name">Lanternvale Summit</span>
    </div>
    <a class="abs brochure-btn" href="#">Request a Brochure ›</a>
    <nav class="abs main-nav">
      <a class="is-active" href="#">Home Solar Panels</a>
      <a href="#">Solar Prices</a>
      <a href="#">Solar Grants</a>
      <a href="#">Solar P.V.</a>
      <a href="#">Get Quotes</a>
    </nav>
  </header>

  <main>
    <div class="abs sheet"></div>

    <div class="abs hero-photo" role="img" aria-label="House roof fitted with solar panels under a blue sky"></div>
    <div class="abs hero-lines">What is sustainable development?<br>Solar power?<br>Green energy</div>
    <div class="abs hero-callout">How can I<br>earn<br>money?</div>

    <div class="abs badge badge-earn"><div class="badge-core"><div style="font-size:31px;line-height:32px;margin-top:30px">Earn</div><div style="font-size:16px;line-height:16px">£455</div><div style="font-size:15px;line-height:16px">a year</div></div></div>
    <div class="abs badge badge-save"><div class="badge-core"><div style="font-size:16px;margin-top:22px">Save</div><div style="font-size:29px;line-height:30px">£180</div><div style="font-size:15px">a year</div></div></div>
    <div class="abs badge badge-avg"><div class="badge-core"><div style="font-size:16px;margin-top:24px">Average</div><div style="font-size:24px;line-height:34px">£6,500</div></div></div>

    <div class="abs thumb thumb-a" role="img" aria-label="Close view of a solar panel array against the sky"></div>
    <div class="abs thumb thumb-b" role="img" aria-label="Ground-mounted solar panels in a field"></div>
    <div class="abs thumb thumb-c" role="img" aria-label="Wind turbines and solar panels above sunflowers"></div>

    <h1 class="abs intro-title">Solar Panels in New Zealand</h1>
    <h2 class="abs intro-sub">Solar Panel Installation for Your Home</h2>

    <section class="abs story story-1">
      <p>Lorem ipsum dolor sit amet, consectetur adipiscing elit. Nullam consectetur odio a sagittis lobortis. Vivamus non lectus id lectus sollicitudin elementum. Praesent pharetra dui id orci semper lobortis. Nunc porta nisi metus, quis consequat nulla bibendum at.&nbsp; Nunc sit amet ultrices dui, Maecenas rhoncus, pulvinar malesuada.</p>
    </section>
    <div class="abs story-photo story-photo-1" role="img" aria-label="House with rooftop solar panels"></div>

    <section class="abs story story-2">
      <h3>Find a Variety of Solar Panels for Less</h3>
      <p>Lorem ipsum dolor sit amet, consectetur adipiscing elit. Nullam consectetur odio a sagittis lobortis. Vivamus non lectus id lectus sollicitudin elementum. Praesent pharetra dui id orci semper lobortis. Nunc porta nisi metus, quis consequat nulla bibendum at.&nbsp; Nunc sit amet ultrices dui, Maecenas rhoncus, pulvinar malesuada. Proin sed fermentum vitae vitae quam.</p>
    </section>
    <div class="abs story-photo story-photo-2" role="img" aria-label="Solar panel reflecting the sky"></div>

    <section class="abs story story-3">
      <h3>Suppliers Of Solar Panels &amp; Solar Power Equipment</h3>
      <p>Lorem ipsum dolor sit amet, consectetur adipiscing elit. Nullam consectetur odio a sagittis lobortis. Vivamus non lectus id lectus sollicitudin elementum. Praesent pharetra dui id orci semper lobortis. Nunc porta nisi metus, quis consequat nulla bibendum at.&nbsp; Nunc sit amet ultrices dui, Maecenas rhoncus, pulvinar malesuada. Nulla sit amet pulvinar sapien.</p>
    </section>
    <div class="abs story-photo story-photo-3" role="img" aria-label="Installers fitting solar panels on a roof"></div>

    <aside class="abs news">
      <div class="news-photo" role="img" aria-label="Rows of solar panels on green grass under a bright sun"></div>
      <div class="news-label">Latest News</div>
      <div class="news-head">Renewable Save and Make You Money</div>
      <div class="news-date">14<br>DEC<br>2013</div>
      <p class="news-text">Quisque volutpat condimentum velit. Class aptent taciti sociosqu ad litora torquent per ...</p>
      <a class="news-more" href="#">▶ ALL NEWS</a>
    </aside>

    <div class="abs helpline" role="img" aria-label="Illustration of a 24-hour phone line against a sunlit sky"></div>
  </main>

  <footer class="abs footer">
    <nav class="footer-links">
      <a href="#">Terms &amp; Conditions</a>
      <a href="#">Privacy Policy</a>
      <a href="#">Sitemap</a>
      <a href="#">Contact Us</a>
    </nav>
    <div class="copyright">© 2013 Lanternvale Holdings <span>| Your Website</span></div>
    <div class="search-field">Search This Site</div>
    <div class="search-go">GO</div>
    <div class="stay-label">Stay in Touch</div>
    <div class="social" aria-label="Social links">
      <span style="background:#3b5b9a"></span>
      <span style="background:#2aa4d8"></span>
      <span style="background:#d8432f"></span>
      <span style="background:#e9e9ee"></span>
      <span style="background:#2a9fd6"></span>
    </div>
  </footer>
</body>
</html>
```